Full Page Ad

We are like looking for something modern, Rustic and unique for a full page ad that includes our logo, office locations, contact information. Please see our webpage and www.BRINKClaimsworks.com. I can send our logo as well.
Updates

Looking for something elegant but industrial, rustic and modern. Added Sunday, June 4, 2017

Industry/Entity Type

Insurance

Font styles to use
Serif

Requirements
Must have
• Contact information

```html
<!DOCTYPE html>
<html lang="en">
<head>
<meta charset="utf-8">
<title>Brink Claimsworks – Full Page Ad</title>
<link rel="stylesheet" href="https://fonts.googleapis.com/css2?family=Montserrat:wght@400;500;600;700;800;900&display=swap">
<style>
  :root {
    --stage: #ecebe8;
    --paper: #ffffff;
    --navy: #1c2d5e;
    --orange: #e27a2b;
    --wood-dark: #4a2a18;
    --wood-mid: #7a4426;
    --wood-light: #a86436;
    --teal: #2f5c66;
    --type-light: #ffffff;
  }
  * { box-sizing: border-box; margin: 0; padding: 0; }
  html, body { width: 1200px; height: 1200px; overflow: hidden; }
  body {
    background: var(--stage);
    font-family: "Montserrat", sans-serif;
    position: relative;
  }
  .ad {
    position: absolute;
    left: 218px;
    top: 20px;
    width: 764px;
    height: 1160px;
    background: var(--paper);
    overflow: hidden;
  }
  .ad-header {
    height: 230px;
    text-align: center;
    padding-top: 52px;
  }
  .brand-name {
    font-weight: 800;
    font-size: 84px;
    line-height: 1;
    letter-spacing: 1px;
    color: var(--navy);
  }
  .brand-descriptor {
    margin-top: 4px;
    font-weight: 500;
    font-size: 15px;
    letter-spacing: 0.5px;
    color: var(--navy);
    text-transform: uppercase;
  }
  .service-line {
    margin-top: 34px;
    font-weight: 700;
    font-size: 17px;
    letter-spacing: 1.6px;
    color: var(--orange);
    text-transform: uppercase;
  }
  .ad-visual {
    position: absolute;
    left: 0; top: 230px;
    width: 764px; height: 930px;
  }
  .wood-wall {
    position: absolute;
    inset: 0;
    background: linear-gradient(160deg, var(--wood-light) 0%, var(--wood-mid) 45%, var(--wood-dark) 100%);
  }
  .lamp-wall {
    position: absolute;
    left: 0; top: 0;
    width: 150px; height: 930px;
    background: linear-gradient(180deg, #34707a, var(--teal) 60%, #1f3f47);
  }
  .office-columns {
    position: absolute;
    top: 311px;
    left: 333px;
    display: flex;
    gap: 20px;
    color: var(--type-light);
  }
  .office-column { width: 204px; display: flex; flex-direction: column; gap: 17px; }
  .office-column.right { margin-top: -19px; gap: 14px; }
  .office-city {
    font-weight: 700;
    font-size: 15px;
    letter-spacing: 0.5px;
    margin-bottom: 10px;
    text-transform: uppercase;
  }
  .office-lines { font-size: 11.5px; line-height: 14px; font-weight: 500; }
  .ad-contact {
    position: absolute;
    right: 14px;
    bottom: 60px;
    text-align: right;
    color: var(--type-light);
    font-weight: 700;
  }
  .ad-contact .phone { font-size: 19px; letter-spacing: 0.5px; }
  .ad-contact .web { font-size: 17px; margin-top: 4px; }
</style>
</head>
<body>
  <main class="ad">
    <header class="ad-header">
      <div class="brand-name">BRINK</div>
      <div class="brand-descriptor">Brink Claimsworks Adjusting Services</div>
      <div class="service-line">24/7 Claim Service • Fast Reporting • Premium Quality</div>
    </header>

    <section class="ad-visual">
      <div class="wood-wall" role="img" aria-label="Photo of a rustic wall of diagonal stained wood planks with industrial pipe lamps and glowing bulbs"></div>
      <div class="lamp-wall" role="img" aria-label="Photo of a teal painted wall with black iron pipe lamp fixtures"></div>
    </section>

    <section class="office-columns">
      <div class="office-column left">
        <article class="office">
          <h2 class="office-city">Albany, NY</h2>
          <p class="office-lines">PO Box 210<br>14 Millstone Road<br>Clifton Park, NY 12000<br>Phone: 518-555-0121<br>Fax: 888-555-0177<br>Toll Free: 1-800-555-0142</p>
        </article>
        <article class="office">
          <h2 class="office-city">Buffalo, NY</h2>
          <p class="office-lines">82 Harbor Street, Suite 210<br>Buffalo, NY 14200<br>Phone: 1-800-555-0142<br>Fax: 888-555-0177</p>
        </article>
        <article class="office">
          <h2 class="office-city">Elmira, NY</h2>
          <p class="office-lines">P.O. Box 318<br>Horseheads, NY 14800<br>Phone: 607-555-0184<br>Fax: 888-555-0177<br>Toll Free: 1-800-555-0142</p>
        </article>
        <article class="office">
          <h2 class="office-city">Long Island, NY</h2>
          <p class="office-lines">P.O. Box 622<br>Rockville Centre, NY 11500<br>Phone: 1-800-555-0142<br>Fax: 888-555-0177<br>Toll Free: 3155550163</p>
        </article>
        <article class="office">
          <h2 class="office-city">Plattsburgh, NY</h2>
          <p class="office-lines">P.O. Box 1940<br>Plattsburgh, NY 12900<br>Phone: 518-555-0121<br>Fax: 888-555-0177<br>Toll Free: 1-800-555-0142</p>
        </article>
        <article class="office">
          <h2 class="office-city">Poughkeepsie, NY</h2>
          <p class="office-lines">9 Beacon Rd<br>Poughkeepsie, NY 12600<br>Phone: 845-555-0159<br>Fax: 888-555-0177<br>Toll Free: 1-800-555-0142</p>
        </article>
      </div>

      <div class="office-column right">
        <article class="office">
          <h2 class="office-city">Queensbury, NY</h2>
          <p class="office-lines">57 Larchmont Lane<br>Queensbury, NY 12800<br>Phone: 518-555-0121<br>Fax: 888-555-0177<br>Toll Free: 1-800-555-0142</p>
        </article>
        <article class="office">
          <h2 class="office-city">Rochester, NY</h2>
          <p class="office-lines">1450B Gristmill Road<br>Suite 320C<br>Rochester, NY 14600<br>Phone: 585-555-0147<br>Fax: 888-555-0177<br>Toll Free: 1-800-555-0142</p>
        </article>
        <article class="office">
          <h2 class="office-city">Springfield, MA</h2>
          <p class="office-lines">P.O. Box 2207<br>240 Walnut St , Ste 2B<br>Springfield, MA 01100<br>Phone: 413-555-0130<br>Fax: 888-555-0177</p>
        </article>
        <article class="office">
          <h2 class="office-city">Syracuse, NY</h2>
          <p class="office-lines">PO Box 5120<br>880 Canal Street<br>Syracuse, NY 13200<br>Phone: 315-555-0168<br>Fax: 888-555-0177<br>Toll Free: 1-800-555-0142</p>
        </article>
        <article class="office">
          <h2 class="office-city">Utica, NY</h2>
          <p class="office-lines">PO Box 3310, Utica, NY 13500<br>6120 Orchard Turnpike<br>Suite 2<br>New Hartford, NY 13400<br>Phone: 315-555-0194<br>Fax: 888-555-0177<br>Toll Free: 1-800-555-0142</p>
        </article>
        <article class="office">
          <h2 class="office-city">Watertown, NY</h2>
          <p class="office-lines">P.O. Box 76<br>Watertown, NY 13600<br>Phone: 315-555-0168<br>Fax: 888-555-0177<br>Toll Free: 1-800-555-0142</p>
        </article>
      </div>
    </section>

    <footer class="ad-contact">
      <div class="phone">1-800-555-0142</div>
      <div class="web">www.BRINKClaimsworks.com</div>
    </footer>
  </main>
</body>
</html>
```